Music Festival in Colorado Needs Awesome Flier Design

We need an eye-catching & captivating flier design for an annual music festival in Denver, CO (USA). The festival features the best Colorado musicians within the genres of jam - funk - bluegrass - electronic - reggae - rock.

The design should look clean and professional while still being creative and unique. The past three years' flier designs are attached, as well as the logo and some other designs that match the aesthetic of what we're looking for.

This festival has a big element of Colorado pride so any

Target Market(s)

Hippies - live music enthusiasts - partiers. Ages 21 - 40.

Industry/Entity Type

Entertainment

Colors
0355a3
ec1f27
ffffff
fbed22

Requirements
Must have
• Attached design text.
Nice to have
• - Quality texture and psychedelic elements.
• - Colorado pride elements; color scheme (red, white, blue & yellow), flag, ect.
• - Nature elements are awesome but this is also a downtown festival so keep that in mind.
Should not have
• Cheesy artwork.

```html
<!DOCTYPE html>
<html lang="en">
<head>
<meta charset="utf-8">
<title>Pass The Sound – Colorado Music Festival</title>
<link rel="stylesheet" href="https://fonts.googleapis.com/css2?family=Righteous&family=Oswald:wght@500&display=swap">
<style>
  :root {
    --white: #f4f1ee;
    --red: #cc1f26;
    --deep-red: #9e1419;
    --sky-navy: #2b3566;
    --sky-purple: #5a4a7a;
    --glow-gold: #d9a23a;
    --moon: #f3efe6;
    --sand-peach: #e8b89c;
    --sand-rust: #b8705a;
  }
  * { margin: 0; padding: 0; box-sizing: border-box; }
  html, body { width: 849px; height: 1200px; overflow: hidden; background: #ffffff; }
  .flier {
    position: relative;
    width: 849px;
    height: 1200px;
    overflow: hidden;
    font-family: "Righteous", sans-serif;
    text-align: center;
  }
  .backdrop {
    position: absolute;
    inset: 0;
    background:
      radial-gradient(circle at 50% 33%, var(--moon) 0 22%, rgba(243,239,230,0.6) 27%, transparent 36%),
      radial-gradient(ellipse at 18% 42%, rgba(217,162,58,0.75) 0, transparent 30%),
      radial-gradient(ellipse at 50% 95%, var(--sand-rust) 0, transparent 60%),
      linear-gradient(180deg, var(--sky-navy) 0%, var(--sky-purple) 20%, #8e7a8a 45%, #b7a7b6 62%, var(--sand-peach) 80%, var(--sand-rust) 100%);
  }
  .dates {
    position: absolute; top: 34px; left: 0; right: 0;
    color: var(--white); font-size: 58px; letter-spacing: 1px; line-height: 1;
  }
  .dates sup { font-size: 22px; vertical-align: 26px; }
  .edition {
    position: absolute; top: 110px; left: 0; right: 0;
    color: var(--white); font-size: 28px;
  }
  .edition sup { font-size: 13px; }
  .festival-name {
    position: absolute; top: 230px; left: 0; right: 0;
    color: var(--red); font-size: 92px; line-height: 0.95; letter-spacing: 2px;
  }
  .festival-tagline {
    position: absolute; top: 430px; left: 0; right: 0;
    color: var(--red); font-family: "Oswald", sans-serif; font-weight: 500;
    font-size: 24px; letter-spacing: 3px; text-transform: uppercase;
  }
  .tickets {
    position: absolute; top: 574px; left: 500px; width: 292px; height: 38px;
    background: var(--red); color: var(--white);
    font-size: 22px; line-height: 38px; letter-spacing: 1px;
  }
  .venue {
    position: absolute; top: 630px; left: 480px; width: 332px;
    color: var(--red); font-size: 22px; line-height: 32px; letter-spacing: 1px;
  }
  .lineup {
    position: absolute; top: 984px; left: 0; right: 0;
    color: var(--deep-red); line-height: 1.25; white-space: nowrap;
  }
  .lineup .tier-1 { font-size: 32px; letter-spacing: 1px; }
  .lineup .tier-2 { font-size: 24px; }
  .lineup .tier-3 { font-size: 19px; }
  .lineup .tier-4 { font-size: 15px; }
  .website {
    position: absolute; top: 1124px; left: 0; right: 0;
    color: var(--white); font-size: 44px; letter-spacing: 2px;
  }
</style>
</head>
<body>
<main class="flier">
  <div class="backdrop" role="img" aria-label="Photo collage: a full moon in a starry purple sky with golden glow, a fist gripping a white electric guitar, over soft desert dunes"></div>

  <p class="dates">MAY 11<sup>TH</sup> - 13<sup>TH</sup> 2018</p>
  <p class="edition">(6<sup>th</sup> Annual)</p>

  <h1 class="festival-name">PASS THE<br>SOUND</h1>
  <p class="festival-tagline">Colorado Music Festival</p>

  <p class="tickets">TICKETS &amp; MORE INFO</p>
  <address class="venue" style="font-style:normal">
    PINE ALLEY YARD<br>
    418 W. 44TH AVE<br>
    DENVER, CO 80216
  </address>

  <section class="lineup">
    <p class="tier-1">JED ALDER BAND, ALLHANDS ORCHESTRA,</p>
    <p class="tier-2">FAULT THEORY, THE LUCKY LENTILS, B-RAE &amp; THE SUMMIT,</p>
    <p class="tier-3">KODIAK, KINETICS, RADIANCE ENSEMBLE, CLOUDSPUN,</p>
    <p class="tier-4">PARAFONIC PAGEANT, CLEAR SIGNAL, RAIL JUNCTION, ORBITS</p>
  </section>

  <p class="website">WWW.PASSTHESOUNDFEST.COM</p>
</main>
</body>
</html>
```